Velmar Ops Business Cards

We need to design some upbeat business cards. We are an Industrial Rope Access Company/Height Safety Company that specialize in Rope Access, Confined Space, Anchor Points, Safety Systems, PPE Inspecions and Rigging.
Company name is Velmar Ops Ltd
Card is for Gareth Lomas the Company Director
His mobile number is 027 418 9072 and email is gareth@velmarops.co.nz. Website address is www.velmarops.co.nz.
We will post some pictures below to ensure you get a good idea of what we do.

```html
<!DOCTYPE html>
<html lang="en">
<head>
<meta charset="utf-8">
<title>Velmar Ops Business Cards</title>
<link href="https://fonts.googleapis.com/css2?family=Russo+One&family=Questrial&display=swap" rel="stylesheet">
<style>
  :root {
    --bg: #e6e6e8;
    --blue-light: #8196d3;
    --blue-mid: #4f67bd;
    --blue-deep: #24398f;
    --brand-blue: #3b55b5;
    --ink: #111111;
    --paper: #ffffff;
    --silver: #eef1fa;
    --band-black: #0c0c0c;
  }
  * { margin: 0; padding: 0; box-sizing: border-box; }
  html, body { width: 1200px; height: 1200px; overflow: hidden; }
  body {
    background: var(--bg);
    position: relative;
    font-family: "Questrial", sans-serif;
  }
  .card {
    position: absolute;
    left: 190px;
    width: 820px;
    height: 470px;
    overflow: hidden;
    box-shadow: 0 10px 28px rgba(0,0,0,0.22);
  }

  /* Back side */
  .card--back {
    top: 90px;
    background: linear-gradient(180deg, var(--blue-light) 0%, var(--blue-mid) 55%, var(--blue-deep) 100%);
    color: var(--silver);
    font-family: "Russo One", sans-serif;
  }
  .card--back .brand {
    position: absolute;
    left: 0; right: 0;
    top: 160px;
    text-align: center;
    font-size: 84px;
    line-height: 1;
    color: var(--silver);
  }
  .services {
    position: absolute;
    list-style: none;
    font-size: 21px;
    line-height: 1.25;
  }
  .services--left { left: 48px; bottom: 40px; }
  .services--left li::before { content: "· "; }
  .services--right { right: 52px; top: 292px; text-align: right; }
  .services--right li::after { content: " ·"; }

  /* Front side */
  .card--front {
    top: 640px;
    background: var(--paper);
    color: var(--ink);
  }
  .card--front .brand {
    position: absolute;
    left: 70px;
    top: 160px;
    font-family: "Russo One", sans-serif;
    font-size: 54px;
    line-height: 1;
    color: var(--brand-blue);
  }
  .person {
    position: absolute;
    right: 60px;
    top: 70px;
    text-align: right;
  }
  .person__name {
    font-size: 42px;
    color: var(--brand-blue);
    letter-spacing: 1px;
    line-height: 1;
  }
  .person__role {
    font-size: 18px;
    margin-top: 4px;
    padding-top: 4px;
    border-top: 1.5px solid var(--ink);
  }
  .divider {
    position: absolute;
    left: 60px;
    right: 60px;
    top: 290px;
    border-top: 1.5px solid var(--ink);
  }
  .contacts {
    position: absolute;
    left: 72px;
    top: 310px;
    list-style: none;
    font-size: 22px;
    line-height: 1.55;
  }
  .contacts li { display: flex; align-items: center; gap: 16px; }
  .contacts svg { width: 22px; height: 22px; fill: var(--brand-blue); flex: none; }
  .band {
    position: absolute;
    left: 0; right: 0; bottom: 0;
    height: 12px;
    display: flex;
  }
  .band__blue { width: 70%; background: var(--blue-deep); }
  .band__black { flex: 1; background: var(--band-black); }
</style>
</head>
<body>

<section class="card card--back">
  <div class="brand">Velmar Ops</div>
  <ul class="services services--right">
    <li>Confined Space</li>
    <li>Safety Systems</li>
    <li>Rigging</li>
  </ul>
  <ul class="services services--left">
    <li>Rope Access</li>
    <li>Anchor Points</li>
    <li>PPE Certification</li>
  </ul>
</section>

<section class="card card--front">
  <div class="brand">Velmar Ops</div>
  <div class="person">
    <div class="person__name">Gareth Lomas</div>
    <div class="person__role">Director</div>
  </div>
  <div class="divider"></div>
  <ul class="contacts">
    <li>
      <svg viewBox="0 0 24 24" aria-hidden="true"><path d="M6.6 10.8a15.1 15.1 0 0 0 6.6 6.6l2.2-2.2a1 1 0 0 1 1-.25 11.4 11.4 0 0 0 3.6.57 1 1 0 0 1 1 1V20a1 1 0 0 1-1 1A17 17 0 0 1 3 4a1 1 0 0 1 1-1h3.5a1 1 0 0 1 1 1c0 1.25.2 2.45.57 3.57a1 1 0 0 1-.25 1z"/></svg>
      027 418 9072
    </li>
    <li>
      <svg viewBox="0 0 24 24" aria-hidden="true"><path d="M12 2a10 10 0 1 0 0 20 10 10 0 0 0 0-20zm6.9 6h-3a15.6 15.6 0 0 0-1.4-3.6A8 8 0 0 1 18.9 8zM12 4c.8 1.2 1.5 2.5 1.9 4h-3.8c.4-1.5 1.1-2.8 1.9-4zM4.3 14a8 8 0 0 1 0-4h3.4a16 16 0 0 0 0 4zm.8 2h3a15.6 15.6 0 0 0 1.4 3.6A8 8 0 0 1 5.1 16zm3-8h-3a8 8 0 0 1 4.4-3.6A15.6 15.6 0 0 0 8.1 8zM12 20c-.8-1.2-1.5-2.5-1.9-4h3.8c-.4 1.5-1.1 2.8-1.9 4zm2.3-6H9.7a14.6 14.6 0 0 1 0-4h4.6a14.6 14.6 0 0 1 0 4zm.2 5.6c.6-1.1 1.1-2.3 1.4-3.6h3a8 8 0 0 1-4.4 3.6zm1.8-5.6a16 16 0 0 0 0-4h3.4a8 8 0 0 1 0 4z"/></svg>
      www.velmarops.co.nz
    </li>
    <li>
      <svg viewBox="0 0 24 24" aria-hidden="true"><path d="M2 5h20v14H2zm2 2v.4l8 5 8-5V7zm0 2.8V17h16V9.8l-8 5z"/></svg>
      gareth@velmarops.co.nz
    </li>
  </ul>
  <div class="band">
    <div class="band__blue"></div>
    <div class="band__black"></div>
  </div>
</section>

</body>
</html>
```